Fight Deflation with Seasonal General Merchandise - Tall Pine Traders & Advisors, Inc.

We are looking to create a Business to Business Advertising Concept that will appear in various trade publications within the US Supermarket Industry. The final concept will be adapted to be used in print, digital and direct mail mediums. For purposes of your submissions, please design as if it is for a 8.5" x 11" (vertical) print ad.

Using the creative elements and images attached for direction and inspiration, please submit your best concepts. The high resolution images shown have already been purchased from a stock photo house with the rights to use them for this campaign. While we like these images as well as the headlines provided, feel free to add your own suggestions or creativity if you wish.

Primarily, however, we'd like you to take the existing headlines and images and build off of them, incorporating solid use of font/text treatment and improving upon overall layout of the ad so that the end result is professional and engaging to the audience.

A note about the concept: Tall Pine Traders supplies US Grocery Store Chains with Seasonal General Merchandise. Currently and for the foreseeable future, grocers are battling the effects of deflationary pricing on key commodities such as Eggs/Dairy; Meat; Produce, etc... The result of this is that grocery prices are significantly lower than last year. While this is good for the consumers, it is not ideal for the retailers as they are making fewer sales and profits while selling the same or more product. The products Tall Pine Trader's sells to these grocers can help the retailer offset these lower prices by adding "incremental" sales and profits to the retailer. Our products range from items like Christmas decor and gift wrap, to outdoor items like patio furniture and grills. We are focusing on the Christmas theme because the ads will drop starting late November.

Target Market(s)

Senior Buyers and Top Executives at US Based Grocery Store Chains.

Industry/Entity Type

Business

Requirements
Must have
• See Project Description
• Open to all colors and fonts.
Nice to have
• See Project Description
Should not have
• See Project Description

```html
<!DOCTYPE html>
<html lang="en">
<head>
<meta charset="utf-8">
<title>Tall Pine Traders and Advisors – Seasonal General Merchandise</title>
<link href="https://fonts.googleapis.com/css2?family=Bebas+Neue&family=Oswald:wght@200;300;400;600&display=swap" rel="stylesheet">
<style>
  :root {
    --red-hot: #e8232b;
    --red-mid: #c41c24;
    --red-deep: #6e0f14;
    --white: #ffffff;
    --ink: #111111;
    --green: #1f9a3c;
    --carton-light: #d9d6d0;
    --carton-dark: #b5b1aa;
  }
  * { margin: 0; padding: 0; box-sizing: border-box; }
  html, body { width: 927px; height: 1200px; overflow: hidden; }
  body { background: var(--red-deep); }
  .ad {
    position: relative;
    width: 927px;
    height: 1200px;
    overflow: hidden;
    background: radial-gradient(ellipse 70% 55% at 62% 30%, var(--red-hot) 0%, var(--red-mid) 45%, var(--red-deep) 100%);
    color: var(--white);
    text-align: center;
  }
  .headline {
    position: absolute;
    top: 46px; left: 0; right: 0;
    font-family: "Bebas Neue", sans-serif;
    font-weight: 400;
    font-size: 66px;
    letter-spacing: 0.5px;
    line-height: 1;
    white-space: nowrap;
  }
  .subhead {
    position: absolute;
    top: 148px; left: 0; right: 0;
    font-family: "Oswald", sans-serif;
    font-weight: 200;
    font-size: 41px;
    line-height: 1.17;
    text-transform: uppercase;
    white-space: nowrap;
  }
  .subhead strong { font-weight: 600; }
  .product-photo {
    position: absolute;
    left: 197px; top: 308px;
    width: 533px; height: 478px;
    border-radius: 14px;
    background: linear-gradient(180deg, var(--carton-light) 0%, var(--carton-dark) 100%);
  }
  .showroom {
    position: absolute;
    top: 820px; left: 0; right: 0;
    font-family: "Oswald", sans-serif;
    font-weight: 300;
    font-size: 21px;
    line-height: 1.47;
    text-transform: uppercase;
    white-space: nowrap;
  }
  .contact {
    position: absolute;
    top: 946px; left: 0; right: 0;
    font-family: "Oswald", sans-serif;
    font-weight: 300;
    font-size: 16px;
    line-height: 1.55;
    text-transform: uppercase;
    white-space: nowrap;
  }
  .brand-plate {
    position: absolute;
    left: 212px; top: 1017px;
    width: 500px; height: 123px;
    background: var(--white);
    border-radius: 22px 22px 0 0;
    display: flex;
    align-items: center;
    justify-content: center;
    gap: 18px;
  }
  .brand-mark { width: 60px; height: 60px; background: var(--ink); }
  .brand-name {
    font-family: "Oswald", sans-serif;
    font-weight: 600;
    font-size: 30px;
    line-height: 1.05;
    color: var(--ink);
    text-align: left;
  }
  .web-band {
    position: absolute;
    left: 0; right: 0; bottom: 0;
    height: 60px;
    background: var(--green);
    font-family: "Oswald", sans-serif;
    font-weight: 400;
    font-size: 27px;
    letter-spacing: 2px;
    line-height: 60px;
    text-transform: uppercase;
    white-space: nowrap;
  }
</style>
</head>
<body>
  <main class="ad">
    <h1 class="headline">Scrambling to deal with deflation?</h1>
    <p class="subhead">Hatch <strong>Eggstraordinary</strong> profits<br>with seasonal general merchandise!</p>

    <div class="product-photo" role="img" aria-label="Open cardboard carton of ten white eggs, one wearing a small red Santa hat"></div>

    <p class="showroom">
      Visit our exciting Fall/Winter 2017 showroom<br>
      Representing over 4,000 items from 350 factories<br>
      Scheduling appointments now for January – March, 2017
    </p>

    <p class="contact">
      Contact Dana Reyes, VP Business Development at<br>
      dreyes@tallpinetraders.com or call 555-014-2290
    </p>

    <div class="brand-plate">
      <span class="brand-mark"></span>
      <span class="brand-name">Tall Pine Traders<br>and Advisors, Inc.</span>
    </div>

    <div class="web-band">www.tallpinetraders.com</div>
  </main>
</body>
</html>
```